Website Graphics

We need 1 page of website graphics for a company called 'RingMeadow.' We are a cloud-based dialing solution for sales agents making outbound calling campaigns. Our software application sits on top of Quillhaven.com and accelerates the entire sales process through automation and multi-line dialing. Our website has a 'Features' page (http://ringmeadow.example/features/) in need of 13 graphics to replace current placeholders.

We would like to see simple designs that blend well with the look and feel of our current website theme, specifically the colors blue, white, and silver. The designs should feel sleek, 3-D, clean, minimalistic, and modern.

For the Feature 'Native Design' (http://ringmeadow.example/features/#tab-id-1) we would like a graphic that shows that our software is extremely secure and reliable.

For the Features 'Preview Mode'(http://ringmeadow.example/features/#tab-id-2), 'Preview Auto' (http://ringmeadow.example/features/#tab-id-3), and 'RingMeadow Mode' (http://ringmeadow.example/features/#tab-id-4), we would like 3-D backdrops of Zentrops and Lumaslates with a screenshot layered on top. I will upload two screen shots. The first can be used for both 'Preview Mode' and 'Preview Auto,' the second is for 'RingMeadow Mode.'

For 'Post-Call Automation' (http://ringmeadow.example/features/#tab-id-5) we are looking for a design that highlights efficiency, speed, and powerful software automation.

For 'Regional ID' (http://ringmeadow.example/features/#tab-id-6) we are looking for a graphic that incorporates a map of North America.

For "Instant Priority Queue' (http://ringmeadow.example/features/#tab-id-9) we are looking for a graphic that shows speed and instant reaction the second a notification comes through.

For 'Live Dashboards' (http://ringmeadow.example/features/#tab-id-10) we are looking for a graphic very similar to the one currently up on the site under that feature. It is a great example of a design that is visually appealing and 3-D.

For the rest of the features, we are open to design interpretations that reflect the description of each feature and help website visitor's visually understand what that feature does.

For reference, here is a website design with graphics that inspire us: http://www.trevik.example/company/what-is-trevik
Updates

Updated brief with detailed descriptions of our vision for each graphic.

Target Market(s)

Professional demographic; companies using Quillhaven.com with sales teams that outbound dial to customers and potential leads.

Industry/Entity Type

Software

Requirements
Must have
• The webpage http://ringmeadow.example/features/ must have 13 images to fill the white space under each feature description.

```html
<!DOCTYPE html>
<html lang="en">
<head>
<meta charset="utf-8">
<title>Features | Prismline Dialer</title>
<link rel="stylesheet" href="https://fonts.googleapis.com/css2?family=Montserrat:wght@600&family=Open+Sans:wght@300;400&family=Lato:wght@400&display=swap">
<style>
:root{
  --brand-blue:#4aafd5;
  --ink:#222;
  --nav-ink:#555;
  --muted:#9a9a9a;
  --body-ink:#666;
  --line:#e2e2e2;
  --footer-band:#dad8db;
  --icon:#7a7a7a;
  --white:#fff;
  --screen-blue:#9fd6ee;
  --silver:#cfd2d5;
}
*{box-sizing:border-box;margin:0;padding:0}
html,body{width:1200px;height:1108px;overflow:hidden;background:var(--white)}
body{position:relative;font-family:"Open Sans",sans-serif;color:var(--ink)}
.top-rule{position:absolute;left:0;top:0;width:1200px;height:18px;border-bottom:1px solid #eee}
.brand{position:absolute;left:110px;top:40px;display:flex;align-items:center;gap:8px}
.brand-mark{width:26px;height:26px;background:var(--brand-blue)}
.brand-name{font-size:15px;font-weight:400;color:var(--brand-blue);letter-spacing:.2px}
.main-nav{position:absolute;top:53px;right:125px;display:flex;gap:24px}
.main-nav a{font-size:12px;letter-spacing:.6px;color:var(--nav-ink);text-decoration:none;text-transform:uppercase}
.main-nav a.is-current{color:var(--ink)}
.page-title{position:absolute;left:0;width:1200px;top:150px;text-align:center;font-family:"Montserrat",sans-serif;font-size:68px;font-weight:600;color:var(--brand-blue);letter-spacing:0;line-height:1}
.page-lede{position:absolute;left:0;width:1200px;top:240px;text-align:center;font-size:19px;font-weight:300;color:var(--brand-blue)}
.feature-tabs{position:absolute;left:110px;top:299px;width:965px;height:578px;border:1px solid var(--line)}
.tab-list{position:absolute;left:0;top:0;width:234px;list-style:none}
.tab-list li{height:44.4px;display:flex;align-items:center;gap:7px;padding-left:15px;font-size:10.5px;font-weight:300;letter-spacing:.3px;color:var(--muted);text-transform:uppercase;border-bottom:1px solid var(--line);border-right:1px solid var(--line)}
.tab-list li:last-child{border-bottom:none}
.tab-list li.is-active{color:var(--ink);font-weight:400;border-right:none}
.tab-list svg{width:11px;height:11px;fill:var(--icon);flex:none}
.tab-list li.is-active svg{fill:#333}
.tab-panel{position:absolute;left:252px;top:0;width:694px}
.tab-copy{margin:19px auto 0;width:600px;text-align:center;font-family:"Lato",sans-serif;font-size:12.5px;line-height:18.5px;color:var(--body-ink)}
.tab-divider{margin-top:19px;border:none;border-top:1px solid var(--line)}
.feature-visual{position:absolute;left:150px;top:226px;width:450px;height:290px}
.feature-visual .shadow{position:absolute;left:10px;top:150px;width:430px;height:140px;border-radius:50%;background:radial-gradient(ellipse at 50% 30%,#dedede 0%,#efefef 45%,rgba(255,255,255,0) 72%)}
.feature-visual .panel{position:absolute;left:110px;top:0;width:240px;height:170px;border-radius:8px;background:linear-gradient(180deg,var(--screen-blue) 0%,#c8e8f5 55%,var(--silver) 100%)}
.site-footer{position:absolute;left:0;top:924px;width:1200px;height:135px;background:var(--footer-band)}
.social-links{position:absolute;left:110px;top:43px;display:flex;gap:7px}
.social-links span{width:30px;height:30px;border-radius:50%;background:#8c8c8c;display:block}
.copyright{position:absolute;left:110px;top:1078px;font-size:11px;color:#333}
</style>
</head>
<body>
<div class="top-rule"></div>

<header>
  <div class="brand"><span class="brand-mark"></span><span class="brand-name">Prismline Dialer</span></div>
  <nav class="main-nav">
    <a class="is-current" href="#">Features</a>
    <a href="#">Native vs. Integrated</a>
    <a href="#">Customers</a>
    <a href="#">Company</a>
    <a href="#">Blog</a>
    <a href="#">Request Demo</a>
  </nav>
</header>

<h1 class="page-title">FEATURES</h1>
<p class="page-lede">Close deals fast with the power of cloud automation and multi-line dialing at your fingertips.</p>

<section class="feature-tabs">
  <ul class="tab-list">
    <li class="is-active"><svg viewBox="0 0 12 12"><rect x="1.5" y="5" width="9" height="7" rx="1"/><path d="M3.5 5V3.5a2.5 2.5 0 0 1 5 0V5h-1.3V3.5a1.2 1.2 0 0 0-2.4 0V5z"/></svg>Native Design</li>
    <li><svg viewBox="0 0 12 12"><circle cx="5" cy="5" r="3.3" fill="none" stroke="#7a7a7a" stroke-width="1.5"/><path d="M7 7.8l1-1 3.5 3.5-1 1z"/></svg>Preview Mode</li>
    <li><svg viewBox="0 0 12 12"><path d="M7 1.5L12 5.5 7 9.5V7C4 7 2 8 .5 10.5 1 6.5 3 4.2 7 4z"/></svg>Preview Auto</li>
    <li><svg viewBox="0 0 12 12"><path d="M2 1l2.2-.3 1.2 2.8-1.4 1a6.5 6.5 0 0 0 3.4 3.4l1-1.4 2.8 1.2L11 10c-5 .8-10-4-9-9z"/></svg>RingMeadow Mode</li>
    <li><svg viewBox="0 0 12 12"><rect x="2.5" y="4" width="7" height="5" rx="1"/><rect x="3" y="1.5" width="6" height="2" rx="1"/><rect x=".5" y="4.2" width="1.4" height="4" rx=".7"/><rect x="10.1" y="4.2" width="1.4" height="4" rx=".7"/><rect x="4" y="9" width="1.4" height="2.5"/><rect x="6.6" y="9" width="1.4" height="2.5"/></svg>Post-Call Automation</li>
    <li><svg viewBox="0 0 12 12"><path d="M6 1l5.5 5H10v5H7.5V8h-3v3H2V6H.5z"/></svg>Regional ID</li>
    <li><svg viewBox="0 0 12 12"><rect x="4" y=".5" width="4" height="7" rx="2"/><path d="M2.5 5.5a3.5 3.5 0 0 0 7 0h1a4.5 4.5 0 0 1-4 4.4V11h2v1h-5v-1h2V9.9a4.5 4.5 0 0 1-4-4.4z"/></svg>Whisper Mode</li>
    <li><svg viewBox="0 0 12 12"><circle cx="4" cy="3.3" r="2.3"/><path d="M0 11c0-3 1.6-4.5 4-4.5S8 8 8 11z"/><circle cx="8.5" cy="3.8" r="1.8"/><path d="M8.7 6.8c2 0 3.3 1.3 3.3 4.2H9c0-1.8-.4-3.2-1.4-4z"/></svg>Live-Call Monitoring</li>
    <li><svg viewBox="0 0 12 12"><path d="M6 .8l5.7 10.4H.3z"/><rect x="5.4" y="4" width="1.2" height="4" fill="#fff"/><rect x="5.4" y="8.8" width="1.2" height="1.2" fill="#fff"/></svg>Instant Priority Queue</li>
    <li><svg viewBox="0 0 12 12"><rect x="1" y="8" width="2.4" height="3.5"/><rect x="4.8" y="5" width="2.4" height="6.5"/><rect x="8.6" y="1.5" width="2.4" height="10"/></svg>Live Dashboards</li>
    <li><svg viewBox="0 0 12 12"><path d="M9 .8l2.2 2.2L4 10.2 1 11l.8-3z"/></svg>Auto Call Recording</li>
    <li><svg viewBox="0 0 12 12"><circle cx="6" cy="6" r="5.3"/><path d="M3.5 3.2c1 .3 1.7 1.2 1.3 2.2-.6 1.2.8 1.6.6 3.2-.1.8-.6 1.6-1.3 1.9M7.5 1.5c-.3 1 .6 1.6 1.5 1.6s1.3 1.4.8 2.3" fill="none" stroke="#fff" stroke-width=".9"/></svg>Global Recycle</li>
    <li><svg viewBox="0 0 12 12"><path d="M4.3 2.5L11 .8v7.5a1.8 1.5 0 1 1-1.2-1.4V3.2L5.5 4.3v5.5A1.8 1.5 0 1 1 4.3 8.4z"/></svg>Music</li>
  </ul>

  <div class="tab-panel">
    <p class="tab-copy">Lorem ipsum dolor sit amet, consectetuer adipiscing elit, sed diam nonummy nibh euismod tincidunt ut eros et accumsan et iusto odio dignissim qui blandit praesent luptatum zzril delenit augue duis dolore te feugait nulla facilisi.</p>
    <hr class="tab-divider">
    <div class="feature-visual" role="img" aria-label="Illustration of a desktop monitor with a pointing hand cursor surrounded by floating message, document, chat and contact icons">
      <div class="shadow"></div>
      <div class="panel"></div>
    </div>
  </div>
</section>

<footer class="site-footer">
  <div class="social-links" aria-label="Social links"><span></span><span></span><span></span></div>
</footer>
<p class="copyright">Copyright © 2014 All Rights Reserved | Prismline Dialer -</p>
</body>
</html>
```